Our Grainfolk - Health and Wellbeing

ABOUT US
we are a supplements and health foods business
Vegan, Lactose, Gluten friendly products
Clean and healthy living approach/mentality

We will be using both 1kg and 500g rectangle bags.
The types of products
Pea Protein
Rice Protein
Hemp Protein
Soy Protein
Creatine
Spirulina

The design needs to be able to facilitate change of product text

1kg
Length: 335 mm
Width: 240 mm
Bottom Gusset: 100 mm

500g
Length: 275 mm
Width: 190 mm
Bottom Gusset: 90 mm

REQUIREMENTS
Digital Banners (inc facebook & Instagram)
Product Label
Branding

CREATIVE IDEAS
colorful and bright
community values, social conscience
crisp/sharp/fresh feeling
dark text with splashes of bright/color throughout
results/success
Use of props, leaves, nature etc.

Target Market(s)

Vegan and health conscience consumers

Industry/Entity Type

Business

Font styles to use
Sans Serif
Decorative
Script

Colors
86cfc6
add136
fbee3e
faa54b
f04a50
33a6d7

Requirements
Must have
• community values, social conscience
• TEXT
• Vegan
• Plant based
• raw
• natural
• gluten free
• Lactose free
• organic ingredients
Nice to have
• Use of props, leaves, nature etc.
• Open to changing the colour scheme of the logo.
• Feature of the text to be around each product, logo secondary on the label.
Should not have
• dark colours
• simple design

```html
<!DOCTYPE html>
<html lang="en">
<head>
<meta charset="utf-8">
<title>Our Grainfolk - Health and Wellbeing - Protein Bag Labels</title>
<link rel="stylesheet" href="https://fonts.googleapis.com/css2?family=Amatic+SC:wght@400;700&family=Montserrat:wght@400;700&family=Special+Elite&display=swap">
<style>
  :root {
    --blue: #1fb0e4;
    --blue-deep: #1a8fc4;
    --coral: #f47a66;
    --paper: #ffffff;
    --ink: #1b1b1b;
    --ribbon: rgba(246, 248, 247, 0.9);
    --band: rgba(240, 242, 240, 0.85);
  }
  * { margin: 0; padding: 0; box-sizing: border-box; }
  html, body { width: 849px; height: 1200px; overflow: hidden; background: var(--paper); }
  .sheet { position: relative; width: 849px; height: 1200px; background: var(--paper); font-family: "Montserrat", sans-serif; }

  .brand { position: absolute; top: 92px; left: 0; width: 849px; text-align: center; }
  .brand-dot { width: 120px; height: 120px; margin: 0 auto; border-radius: 50%; background: var(--blue); }
  .brand-name { margin-top: 22px; font-weight: 700; font-size: 48px; color: var(--blue); letter-spacing: 0.5px; line-height: 1; }

  .bag { position: absolute; top: 362px; width: 405px; height: 822px; overflow: hidden; }
  .bag--pea { left: 18px; --accent: var(--blue); }
  .bag--rice { left: 431px; --accent: var(--coral); }

  .bag-photo { position: absolute; left: 0; top: 0; width: 405px; height: 630px; }
  .bag--pea .bag-photo { background: linear-gradient(90deg, #6f9a5a 0%, #9cc684 40%, #4d9a2c 75%, #8fce55 100%); }
  .bag--rice .bag-photo { background: linear-gradient(180deg, #b8bdb6 0%, #8e9a86 20%, #86b04a 38%, #5d8f24 70%, #3f6e1a 100%); }

  .ribbon { position: absolute; left: 126px; top: 0; width: 154px; height: 412px; }
  .ribbon-text { position: absolute; left: 126px; top: 0; width: 154px; text-align: center; color: var(--accent); font-family: "Amatic SC", cursive; }
  .ornament { display: block; margin: 0 auto; width: 90px; height: 34px; border-radius: 40px 40px 8px 8px; background: var(--accent); opacity: 0.35; }
  .ornament--top { margin-top: 30px; }
  .ornament--bottom { margin-top: 6px; border-radius: 8px 8px 40px 40px; }
  .rule { width: 96px; height: 2px; margin: 4px auto; background: var(--accent); }
  .word-organic { font-size: 42px; line-height: 48px; font-weight: 400; }
  .word-product { font-size: 112px; line-height: 100px; font-weight: 400; letter-spacing: 4px; }
  .word-protein { font-size: 44px; line-height: 48px; font-weight: 400; }
  .claims { font-size: 12px; font-weight: 700; letter-spacing: 0.5px; line-height: 16px; }

  .band { position: absolute; left: 0; top: 504px; width: 405px; height: 44px; background: var(--band); }
  .icon { position: absolute; top: 510px; width: 28px; height: 28px; border-radius: 50%; background: var(--accent); box-shadow: 0 1px 3px rgba(0,0,0,0.25); color: #fff; font-size: 10px; font-weight: 700; display: flex; align-items: center; justify-content: center; }
  .icon svg { width: 14px; height: 14px; }
  .captions { position: absolute; top: 566px; font-size: 7px; color: rgba(255,255,255,0.85); }
  .captions--left { left: 12px; }
  .captions--right { right: 10px; }

  .seal { position: absolute; left: 126px; top: 446px; width: 152px; height: 152px; }
  .seal-name { position: absolute; left: 126px; top: 512px; width: 152px; text-align: center; font-weight: 700; font-size: 14px; color: var(--accent); }
  .seal-dot { position: absolute; left: 190px; top: 478px; width: 26px; height: 26px; border-radius: 50%; background: var(--accent); }

  .gusset { position: absolute; left: 0; top: 630px; width: 405px; height: 192px; background: var(--accent); display: flex; align-items: center; justify-content: center; }
  .gusset-label { font-family: "Special Elite", monospace; font-size: 27px; color: var(--ink); }
</style>
</head>
<body>
<main class="sheet">
  <header class="brand">
    <div class="brand-dot"></div>
    <div class="brand-name">Our Grainfolk</div>
  </header>

  <section class="bag bag--pea">
    <div class="bag-photo" role="img" aria-label="Photograph of pea plant flowers and dewy green leaves"></div>
    <svg class="ribbon" viewBox="0 0 154 412">
      <path d="M0 0 H154 V330 L77 410 L0 330 Z" fill="var(--ribbon)" stroke="var(--accent)" stroke-width="1.5"/>
    </svg>
    <div class="ribbon-text">
      <span class="ornament ornament--top" role="img" aria-label="Decorative floral flourish"></span>
      <div class="rule"></div>
      <div class="word-organic">Organic</div>
      <div class="rule"></div>
      <div class="word-product">Pea</div>
      <div class="word-protein">Protein</div>
      <div class="rule"></div>
      <div class="claims">RAW | VEGAN | GLUTEN FREE</div>
      <div class="rule"></div>
      <span class="ornament ornament--bottom" role="img" aria-label="Decorative floral flourish"></span>
    </div>
    <div class="band"></div>
    <div class="icon" style="left:10px">O</div>
    <div class="icon" style="left:48px"><svg viewBox="0 0 14 14"><path d="M3 11 C3 5 7 3 12 3 C12 8 9 11 3 11 Z M3 11 L8 6" fill="none" stroke="#fff" stroke-width="1.5"/></svg></div>
    <div class="icon" style="left:86px">V</div>
    <div class="icon" style="left:290px">GF</div>
    <div class="icon" style="left:328px"><svg viewBox="0 0 14 14"><path d="M7 13 V3 M7 5 L4 3 M7 5 L10 3 M7 8 L4 6 M7 8 L10 6" fill="none" stroke="#fff" stroke-width="1.5"/></svg></div>
    <div class="icon" style="left:366px">LF</div>
    <div class="captions captions--left">Organic | Plant Based | Vegan</div>
    <div class="captions captions--right">Gluten Free | Raw | Lactose Free</div>
    <svg class="seal" viewBox="0 0 152 152">
      <circle cx="76" cy="76" r="74" fill="var(--ribbon)" stroke="var(--accent)" stroke-width="3"/>
      <circle cx="76" cy="76" r="64" fill="none" stroke="var(--accent)" stroke-width="3" stroke-dasharray="4 3"/>
      <circle cx="76" cy="76" r="57" fill="none" stroke="var(--accent)" stroke-width="1.5"/>
    </svg>
    <div class="seal-dot"></div>
    <div class="seal-name">Our Grainfolk</div>
    <div class="gusset"><span class="gusset-label">Gusset</span></div>
  </section>

  <section class="bag bag--rice">
    <div class="bag-photo" role="img" aria-label="Photograph of a dewy green rice field with misty trees behind"></div>
    <svg class="ribbon" viewBox="0 0 154 412">
      <path d="M0 0 H154 V330 L77 410 L0 330 Z" fill="var(--ribbon)" stroke="var(--accent)" stroke-width="1.5"/>
    </svg>
    <div class="ribbon-text">
      <span class="ornament ornament--top" role="img" aria-label="Decorative floral flourish"></span>
      <div class="rule"></div>
      <div class="word-organic">Organic</div>
      <div class="rule"></div>
      <div class="word-product">Rice</div>
      <div class="word-protein">Protein</div>
      <div class="rule"></div>
      <div class="claims">RAW | VEGAN | GLUTEN FREE</div>
      <div class="rule"></div>
      <span class="ornament ornament--bottom" role="img" aria-label="Decorative floral flourish"></span>
    </div>
    <div class="band"></div>
    <div class="icon" style="left:10px">O</div>
    <div class="icon" style="left:48px"><svg viewBox="0 0 14 14"><path d="M3 11 C3 5 7 3 12 3 C12 8 9 11 3 11 Z M3 11 L8 6" fill="none" stroke="#fff" stroke-width="1.5"/></svg></div>
    <div class="icon" style="left:86px">V</div>
    <div class="icon" style="left:290px">GF</div>
    <div class="icon" style="left:328px"><svg viewBox="0 0 14 14"><path d="M7 13 V3 M7 5 L4 3 M7 5 L10 3 M7 8 L4 6 M7 8 L10 6" fill="none" stroke="#fff" stroke-width="1.5"/></svg></div>
    <div class="icon" style="left:366px">LF</div>
    <div class="captions captions--left">Organic | Plant Based | Vegan</div>
    <div class="captions captions--right">Gluten Free | Raw | Lactose Free</div>
    <svg class="seal" viewBox="0 0 152 152">
      <circle cx="76" cy="76" r="74" fill="var(--ribbon)" stroke="var(--accent)" stroke-width="3"/>
      <circle cx="76" cy="76" r="64" fill="none" stroke="var(--accent)" stroke-width="3" stroke-dasharray="4 3"/>
      <circle cx="76" cy="76" r="57" fill="none" stroke="var(--accent)" stroke-width="1.5"/>
    </svg>
    <div class="seal-dot"></div>
    <div class="seal-name">Our Grainfolk</div>
    <div class="gusset"><span class="gusset-label">Gusset</span></div>
  </section>
</main>
</body>
</html>
```